Zarvo! Next Steps?, Bail Bond Company Check-in App , Court date, Court Reminders, Payments

Zarvo!
Next Steps?
WINNER OF THIS CONTEST WILL HAVE OPPORTUNITY TO DESIGN CUSTOMIZE SOME OUR COMPANY PAGES AFTER CONTEST!
Check-in with your Bail agent via pic/video
Receive Court reminders
Make a payments

Basically this app is a portal to 3rd party bail companies.
The idea is for the person whom makes bail downloads the Zarvo app from App Store.
Then they select a bail bond company.
This would be similar to a restaurant, real estate agent, insurance agent,,app where we could populate bail bond companies by client location or by typing in name of bail company.
We would like the ability to customize each bail bond company landing pages but are open to a global concept. when you click the bail bond company location it would have the logos for that company so the bail bond company screens would need to be customizeble
The app will require a photo or video check-in that is date and time
stamped with a gps location stored in check-in history
Check-in can be scheduled or random or voluntary
Voluntary and Scheduled Check-ins would require check-in button
Random would be via alert or text

The app should be able to receive court date updates
The app should allow clients to make payments to bail bond company
we need
ZARVO! landing page
client registration screens, check-in screens, available bail bond company screens for client to choose from
client registration page should include
name
email address
phone number
picture
home address
work address
date of birth
this app is different from our u-trak app. this is a bail bond check-in app for third party bail bond companies.
landing page should be ZARVO! Next Steps?
ZARVO ! Registration
Find your bail bond Company should list bail bond companies near me and search bar for searching bail bond companies by name
Next landing pages would be customizable for the third party bail bond companies
these would include pages for
check-ins via pics/videos
payment page
court reminders
contact information for bail bond companies
Zarvo Pages include
initial landing page
registration page
search bail companies

Bail bond company pages should include
Bali bond company landing page
Use KELNOR BAIL BOND COMPANY as example
contact information for bail company
check-in page
payment page
court reminder page
Updates

Low designer entries

Low designer entries

Sick

Sick

Sick

Target Market(s)

Court Defendants, Probation ,jails, sheriffs, judges, attorneys

Industry/Entity Type

justice, law enforcement, courts,

Requirements
Must have
• Check-in via pic/video, ability to receive court date reminders, make paymentswe need client registration screens, check-in screens, available bail bond company screens for client to choose from
Nice to have
• Professional easy to navigate intuitive customizable to 3rd party bail bond companies, logos,phone numbers etc.
Should not have
• unprofessional graphics,

```html
<!DOCTYPE html>
<html lang="en">
<head>
<meta charset="utf-8">
<title>Zarvo! Next Steps? – App Screens</title>
<link rel="stylesheet" href="https://fonts.googleapis.com/css2?family=Jost:wght@400;500;600;700;800&family=Cabin:wght@400;500;600&display=swap">
<style>
:root{
  --navy:#1f4380;
  --navy-deep:#183869;
  --screen:#eef4fc;
  --page:#ffffff;
  --line:#8fa3c4;
  --label:#6f86ad;
  --muted:#5c6f8f;
  --chip:#c5d3e8;
  --search:#d3deed;
  --alert:#c23a2e;
  --gold:#f2a33a;
  --ink:#1d2a40;
}
*{box-sizing:border-box;margin:0;padding:0}
html,body{width:1200px;height:1200px;overflow:hidden;background:var(--page)}
body{position:relative;font-family:"Cabin",sans-serif;color:var(--ink)}
.screen{position:absolute;width:245px;height:536px;border-radius:26px;background:var(--screen);overflow:hidden;box-shadow:0 10px 28px rgba(31,67,128,.14)}
.abs{position:absolute}
.heading{font-family:"Jost",sans-serif;color:var(--navy);line-height:1}
.back{position:absolute;left:9px;top:36px;width:18px;height:10px}
.page-title{position:absolute;left:11px;font-family:"Jost",sans-serif;color:var(--navy);font-size:19px;line-height:20px;font-weight:400}
.page-title b{font-weight:700;display:block}
.pill{position:absolute;border-radius:22px;background:var(--navy);color:#fff;display:flex;align-items:center;justify-content:center;font-family:"Cabin",sans-serif;box-shadow:0 6px 12px rgba(31,67,128,.28)}
.pill svg{margin-left:14px}

/* landing */
.landing-photo{position:absolute;left:0;top:0;width:245px;height:380px;background:linear-gradient(180deg,#7d8796 0%,#9aa3b0 45%,#c7d0de 75%,var(--screen) 100%)}
.brand-mark{position:absolute;left:50px;top:53px;width:156px;height:156px;border-radius:50%;background:#b9a07a;display:flex;align-items:center;justify-content:center}
.brand-mark span{font-family:"Jost",sans-serif;font-weight:700;font-size:30px;color:#fff;letter-spacing:1px}
.hero{position:absolute;left:11px;top:282px;font-family:"Jost",sans-serif;font-weight:800;color:var(--navy);font-size:58px;line-height:54px;letter-spacing:-1px}
.hero-sub{position:absolute;left:12px;top:389px;font-family:"Jost",sans-serif;color:var(--navy);font-size:22px}
.btn-land{position:absolute;top:451px;width:102px;height:35px;border-radius:7px;background:var(--navy);color:#fff;font-family:"Jost",sans-serif;font-size:11px;display:flex;align-items:center;justify-content:center;box-shadow:0 6px 10px rgba(31,67,128,.3)}
.btn-land.soft{background:linear-gradient(180deg,#3466a8,#22508f)}

/* registration */
.field{position:absolute;left:8px;width:222px;height:33px;border:1px solid var(--line);border-radius:5px}
.field .lbl{position:absolute;left:14px;top:-7px;padding:0 8px;background:var(--screen);font-family:"Jost",sans-serif;font-weight:500;font-size:8.5px;color:var(--label);letter-spacing:.2px}
.field .ph{position:absolute;left:32px;top:16px;font-size:7.5px;color:var(--muted)}
.field .val{position:absolute;left:32px;top:8px;font-size:13px;color:var(--ink)}
.icon-btn{position:absolute;top:269px;width:36px;height:33px;border-radius:5px;background:var(--navy);display:flex;align-items:center;justify-content:center}
.icon-btn.light{background:#2e5d9e}
.agree{position:absolute;left:8px;top:458px;display:flex;align-items:center;font-size:7.5px;color:var(--muted)}
.agree .box{width:16px;height:16px;border-radius:3px;background:#a9b8d2;margin-right:11px}
.agree a{color:var(--navy);text-decoration:underline;margin:0 2px}

/* home */
.avatar{position:absolute;border-radius:50%;background:linear-gradient(160deg,#6e7f95,#2c3644)}
.greet{position:absolute;left:52px;top:54px}
.greet small{display:block;font-size:7px;color:var(--muted)}
.greet strong{display:block;font-size:9.5px;font-weight:500;color:var(--ink);margin-top:2px}
.search{position:absolute;left:9px;top:103px;width:222px;height:37px;border-radius:5px;background:var(--search)}
.search span{position:absolute;left:32px;top:14px;font-size:7.5px;color:var(--muted)}
.kicker{position:absolute;left:9px;font-family:"Jost",sans-serif;font-weight:600;font-size:7px;color:var(--label)}
.sect{position:absolute;left:9px;font-family:"Jost",sans-serif;font-weight:700;font-size:21px;color:var(--navy);line-height:1}
.view-all{position:absolute;left:207px;font-size:7px;color:var(--muted)}
.chip{position:absolute;top:200px;height:20px;border-radius:6px;background:var(--chip);color:var(--navy);font-size:10px;display:flex;align-items:center;justify-content:center}
.chip.on{background:var(--navy);color:#fff}
.company-card{position:absolute;top:287px;width:121px;height:78px;border-radius:7px;overflow:hidden;box-shadow:0 4px 10px rgba(0,0,0,.18)}
.company-card .label{position:absolute;left:8px;bottom:8px;color:#fff;font-size:7px;font-family:"Cabin",sans-serif}
.company-card .badge{position:absolute;left:0;top:8px;padding:1px 9px 1px 7px;background:var(--gold);color:#fff;font-size:8px;font-weight:600;clip-path:polygon(0 0,100% 0,88% 50%,100% 100%,0 100%)}
.company-card .dot{position:absolute;right:6px;top:8px;width:26px;height:26px;border-radius:50%;background:rgba(255,255,255,.85)}
.rec-name{position:absolute;left:52px;top:447px;font-family:"Jost",sans-serif;font-weight:600;font-size:7.5px;color:var(--label)}
.tabbar{position:absolute;width:233px;height:47px;border-radius:22px;background:var(--navy);display:flex;justify-content:space-around;align-items:center;padding:0 10px;box-shadow:0 6px 14px rgba(31,67,128,.3)}
.tab{display:flex;flex-direction:column;align-items:center;font-size:6.5px;color:#7f9cc9}
.tab svg{margin-bottom:5px}
.tab.on{color:#fff}

/* check-ins */
.capture{position:absolute;left:60px;width:128px;height:104px;border:1px solid var(--line);border-radius:4px;background:linear-gradient(180deg,#dfe7f3,#b8c6dc);display:flex;align-items:center;justify-content:center}

/* company */
.company-photo{position:absolute;left:0;top:0;width:245px;height:310px;background:linear-gradient(160deg,#4d4437 0%,#8b7556 40%,#b3946a 65%,#c9b397 100%)}
.detail-card{position:absolute;left:0;top:216px;width:245px;height:100px;border-radius:20px 20px 0 0;background:linear-gradient(180deg,rgba(222,214,200,.92) 0%,rgba(232,236,242,.96) 70%,var(--screen) 100%)}
.back-chip{position:absolute;left:7px;top:32px;width:24px;height:16px;border-radius:4px;background:rgba(238,244,252,.8)}
.co-name{position:absolute;left:17px;top:232px;font-family:"Jost",sans-serif;font-weight:700;font-size:11.5px;color:var(--navy)}
.co-state{position:absolute;left:17px;top:252px;font-size:10px;color:var(--ink)}
.feat{position:absolute;left:72px;top:254px;width:56px;height:12px;background:var(--gold);color:#fff;font-size:8px;font-weight:600;display:flex;align-items:center;padding-left:7px;clip-path:polygon(0 0,100% 0,92% 50%,100% 100%,0 100%)}
.stars{position:absolute;left:17px;top:268px;font-size:9px;color:var(--navy);letter-spacing:2px}
.stars span{letter-spacing:0;color:var(--ink);font-size:8.5px}
.desc-title{position:absolute;left:17px;top:296px;font-family:"Jost",sans-serif;font-weight:700;font-size:11.5px;color:var(--navy)}
.desc{position:absolute;left:17px;top:313px;width:215px;font-size:10px;line-height:13.4px;color:var(--ink)}
.address{position:absolute;left:40px;top:383px;font-size:10px;line-height:13.5px;color:var(--ink)}
.action{position:absolute;top:430px;width:97px;height:28px;border-radius:14px;background:var(--navy);color:#fff;font-family:"Jost",sans-serif;font-weight:600;font-size:10.5px;display:flex;align-items:center;justify-content:center;box-shadow:0 5px 10px rgba(31,67,128,.28)}

/* reminders */
.reminder{position:absolute;left:9px}
.reminder .when{font-family:"Jost",sans-serif;font-weight:600;font-size:11px;color:var(--navy)}
.reminder .gps{font-size:7.5px;color:var(--muted);margin-top:2px;word-spacing:6px}
.reminder.urgent .when,.reminder.urgent .gps{color:var(--alert)}
</style>
</head>
<body>

<!-- Landing -->
<section class="screen" style="left:84px;top:37px">
  <div class="landing-photo" role="img" aria-label="Black and white photo of a judge's gavel on a wooden block"></div>
  <div class="brand-mark"><span>KELNOR</span></div>
  <div class="hero">ZARVO!</div>
  <div class="hero-sub">NEXT STEPS?</div>
  <div class="btn-land soft" style="left:14px">ZARVO!</div>
  <div class="btn-land" style="left:129px">REGISTER</div>
</section>

<!-- Registration -->
<section class="screen" style="left:472px;top:37px">
  <svg class="back" viewBox="0 0 18 10" fill="none" stroke="#1f4380" stroke-width="1.2"><path d="M17 5H1M5 1 1 5l4 4"/></svg>
  <div class="page-title" style="top:62px">CREATE A NEW<b>ACCOUNT</b></div>
  <div class="field" style="top:125px"><span class="lbl">NAME</span><span class="val">Marisol Dunleavy</span></div>
  <div class="field" style="top:173px"><span class="lbl">EMAIL ADDRESS</span><span class="ph">Your email address</span></div>
  <div class="field" style="top:221px"><span class="lbl">MOBILE #</span><span class="ph">Your mobile number</span></div>
  <div class="field" style="top:269px;width:128px"><span class="lbl">PICTURE</span><span class="ph">Upload your picture</span></div>
  <div class="icon-btn light" style="left:147px"><svg width="14" height="14" viewBox="0 0 14 14" fill="none" stroke="#fff" stroke-width="1.3"><circle cx="6" cy="6" r="4.5"/><path d="m9.5 9.5 3.5 3.5"/></svg></div>
  <div class="icon-btn" style="left:194px"><svg width="15" height="13" viewBox="0 0 15 13" fill="none" stroke="#fff" stroke-width="1.2"><path d="M1 4h3l1.5-2h4L11 4h3v8H1z"/><circle cx="7.5" cy="7.5" r="2.5"/></svg></div>
  <div class="field" style="top:317px"><span class="lbl">HOME ADDRESS</span><span class="ph">Your home address</span></div>
  <div class="field" style="top:366px"><span class="lbl">WORK ADDRESS</span><span class="ph">Work address</span></div>
  <div class="field" style="top:414px"><span class="lbl">DATE OF BIRTH</span><span class="ph">Your date of birth</span></div>
  <div class="agree"><span class="box"></span>I agree <a>Privacy</a> | <a>Terms &amp; Concition</a></div>
  <div class="pill" style="left:125px;top:485px;width:105px;height:37px;font-size:12px">Register<svg width="11" height="9" viewBox="0 0 11 9" fill="none" stroke="#fff" stroke-width="1.2"><path d="M0 4.5h10M6 .5l4 4-4 4"/></svg></div>
</section>

<!-- Home -->
<section class="screen" style="left:854px;top:37px">
  <div class="avatar" style="left:10px;top:47px;width:32px;height:32px" role="img" aria-label="Profile photo of the user"></div>
  <div class="greet"><small>Good Morning</small><strong>Marisol Dunleavy</strong></div>
  <svg class="abs" style="left:219px;top:59px" width="13" height="9" viewBox="0 0 13 9" fill="none" stroke="#1f4380" stroke-width="1.4"><path d="M0 1h13M3 4.5h10M0 8h13"/></svg>
  <div class="search">
    <svg class="abs" style="left:10px;top:12px" width="13" height="13" viewBox="0 0 13 13" fill="none" stroke="#1f4380" stroke-width="1.2"><circle cx="5.5" cy="5.5" r="4.5"/><path d="m9 9 3.5 3.5"/></svg>
    <span>Search bail companies</span>
    <svg class="abs" style="left:199px;top:12px" width="13" height="13" viewBox="0 0 13 13" fill="none" stroke="#1f4380" stroke-width="1.1"><path d="M1 1h11L7.5 6.5V12L5.5 10.5v-4z"/></svg>
  </div>
  <div class="kicker" style="top:162px">BAIL BOND</div>
  <div class="sect" style="top:172px">SERVICES</div>
  <div class="view-all" style="top:182px">View all</div>
  <div class="chip on" style="left:9px;width:70px">Immigration</div>
  <div class="chip" style="left:86px;width:70px">Larceny/theft</div>
  <div class="chip" style="left:164px;width:48px">Juvenile</div>
  <div class="chip" style="left:220px;width:40px;justify-content:flex-start;padding-left:10px">Bur</div>
  <div class="kicker" style="top:247px">BAIL BOND</div>
  <div class="sect" style="top:258px">NEAR BY</div>
  <div class="view-all" style="top:269px">View all</div>
  <div class="company-card" style="left:9px;background:linear-gradient(160deg,#2b3447,#5a4a3e 60%,#22262f)" role="img" aria-label="Night city skyline behind a hand holding a phone">
    <span class="dot"></span><span class="label">BAIL BOND COMPANY</span>
  </div>
  <div class="company-card" style="left:143px;background:linear-gradient(160deg,#cfd5dc,#8d96a2 60%,#4f5866)" role="img" aria-label="Courthouse columns">
    <span class="badge">Featured</span><span class="dot"></span><span class="label">BAIL BOND COMPANY</span>
  </div>
  <div class="kicker" style="top:392px">BAIL BOND</div>
  <div class="sect" style="top:403px">RECOMENDED</div>
  <div class="view-all" style="top:414px">View all</div>
  <div class="avatar" style="left:10px;top:435px;width:32px;height:32px;background:linear-gradient(160deg,#5fa3a6,#1d3d45)" role="img" aria-label="Company building photo"></div>
  <div class="rec-name">BAIL BOND COMPANY</div>
  <svg class="abs" style="left:216px;top:446px" width="15" height="10" viewBox="0 0 15 10" fill="none" stroke="#1f4380" stroke-width="1.2"><path d="M1 5s2.5-4 6.5-4S14 5 14 5s-2.5 4-6.5 4S1 5 1 5z"/><circle cx="7.5" cy="5" r="2"/></svg>
  <nav class="tabbar" style="left:5px;top:474px">
    <div class="tab on"><svg width="13" height="13" viewBox="0 0 13 13" fill="none" stroke="#fff" stroke-width="1.2"><path d="M1 6 6.5 1 12 6v6H1z"/><path d="M5 12V8h3v4"/></svg>Home</div>
    <div class="tab"><svg width="11" height="13" viewBox="0 0 11 13" fill="none" stroke="#7f9cc9" stroke-width="1.1"><path d="M5.5 12S1 7.5 1 5a4.5 4.5 0 0 1 9 0c0 2.5-4.5 7-4.5 7z"/><circle cx="5.5" cy="5" r="1.6"/></svg>Check-In</div>
    <div class="tab"><svg width="14" height="11" viewBox="0 0 14 11" fill="none" stroke="#7f9cc9" stroke-width="1.1"><rect x=".5" y=".5" width="13" height="10" rx="1"/><path d="M.5 4h13"/></svg>Payment</div>
    <div class="tab"><svg width="12" height="13" viewBox="0 0 12 13" fill="none" stroke="#7f9cc9" stroke-width="1.1"><path d="M2 9V5.5a4 4 0 0 1 8 0V9l1 1.5H1z"/><path d="M5 12h2"/></svg>Court Reminder</div>
  </nav>
</section>

<!-- Check-ins -->
<section class="screen" style="left:84px;top:629px">
  <svg class="back" viewBox="0 0 18 10" fill="none" stroke="#1f4380" stroke-width="1.2"><path d="M17 5H1M5 1 1 5l4 4"/></svg>
  <div class="page-title" style="top:61px">YOUR<b>CHECK-INS</b></div>
  <div class="capture" style="top:142px"><svg width="26" height="24" viewBox="0 0 26 24" fill="none" stroke="#1f4380" stroke-width="1.2"><rect x="1" y="1" width="24" height="22"/><circle cx="8" cy="7" r="2"/><path d="m1 20 8-7 5 4 4-4 7 6"/></svg></div>
  <div class="capture" style="top:284px"><svg width="30" height="20" viewBox="0 0 30 20" fill="none" stroke="#1f4380" stroke-width="1.2"><rect x="1" y="1" width="19" height="18"/><path d="m20 8 9-6v16l-9-6"/></svg></div>
  <div class="pill" style="left:129px;top:485px;width:105px;height:37px;font-size:12px">Check-ins<svg width="11" height="9" viewBox="0 0 11 9" fill="none" stroke="#fff" stroke-width="1.2"><path d="M0 4.5h10M6 .5l4 4-4 4"/></svg></div>
</section>

<!-- Company profile -->
<section class="screen" style="left:469px;top:629px">
  <div class="company-photo" role="img" aria-label="Photo of brass scales of justice and a gavel on a wooden desk"></div>
  <div class="back-chip"></div>
  <svg class="abs" style="left:10px;top:35px" width="18" height="10" viewBox="0 0 18 10" fill="none" stroke="#1f4380" stroke-width="1.2"><path d="M17 5H1M5 1 1 5l4 4"/></svg>
  <div class="detail-card"></div>
  <div class="co-name">KELNOR BAIL BOND COMPANY</div>
  <svg class="abs" style="left:215px;top:236px" width="14" height="12" viewBox="0 0 14 12" fill="none" stroke="#fff" stroke-width="1.2"><path d="M7 11 1.8 6A3 3 0 0 1 7 2a3 3 0 0 1 5.2 4z"/></svg>
  <div class="co-state">Tennessee</div>
  <div class="feat">Featured</div>
  <div class="stars">★★★★★ <span>(4.9)</span></div>
  <div class="desc-title">DESCRIPTION</div>
  <p class="desc">This bonding company makes it hassle free and simplifies the requirements to ease one in such a stressful situation for the loved one making the bond</p>
  <svg class="abs" style="left:17px;top:389px" width="12" height="14" viewBox="0 0 12 14" fill="none" stroke="#1f4380" stroke-width="1.1"><path d="M6 13S1 8 1 5.3a5 5 0 0 1 10 0C11 8 6 13 6 13z"/><circle cx="6" cy="5.3" r="1.8"/></svg>
  <div class="address">418 W. Harlow Lane<br>Brookfield 60513 Oregon</div>
  <div class="action" style="left:17px">(555) 014-2290</div>
  <div class="action" style="left:129px">POST A BAIL</div>
  <nav class="tabbar" style="left:6px;top:472px">
    <div class="tab on"><svg width="13" height="13" viewBox="0 0 13 13" fill="none" stroke="#fff" stroke-width="1.2"><path d="M1 6 6.5 1 12 6v6H1z"/><path d="M5 12V8h3v4"/></svg>Home</div>
    <div class="tab"><svg width="11" height="13" viewBox="0 0 11 13" fill="none" stroke="#7f9cc9" stroke-width="1.1"><path d="M5.5 12S1 7.5 1 5a4.5 4.5 0 0 1 9 0c0 2.5-4.5 7-4.5 7z"/><circle cx="5.5" cy="5" r="1.6"/></svg>Check-In</div>
    <div class="tab"><svg width="14" height="11" viewBox="0 0 14 11" fill="none" stroke="#7f9cc9" stroke-width="1.1"><rect x=".5" y=".5" width="13" height="10" rx="1"/><path d="M.5 4h13"/></svg>Payment</div>
    <div class="tab"><svg width="12" height="13" viewBox="0 0 12 13" fill="none" stroke="#7f9cc9" stroke-width="1.1"><path d="M2 9V5.5a4 4 0 0 1 8 0V9l1 1.5H1z"/><path d="M5 12h2"/></svg>Court Reminder</div>
  </nav>
</section>

<!-- Court reminders -->
<section class="screen" style="left:854px;top:629px">
  <svg class="back" viewBox="0 0 18 10" fill="none" stroke="#1f4380" stroke-width="1.2"><path d="M17 5H1M5 1 1 5l4 4"/></svg>
  <div class="page-title" style="top:61px">COURT<b>REMINDERS</b></div>
  <div class="reminder" style="top:165px"><div class="when">Thus, Sep 3rd at 1:00 p.m.</div><div class="gps">33° 52′ 7.413″ S | 152° 32′ 31.513″ E</div></div>
  <div class="reminder" style="top:213px"><div class="when">Thus, Aug 8th at 2:00 p.m.</div><div class="gps">33° 52′ 7.413″ S | 152° 32′ 31.513″ E</div></div>
  <div class="reminder urgent" style="top:261px"><div class="when">Thus, Jul 4th at 1:00 p.m.</div><div class="gps">33° 52′ 7.413″ S | 152° 32′ 31.513″ E</div></div>
  <div class="reminder" style="top:310px"><div class="when">Thus, Jun 6th at 3:00 p.m.</div><div class="gps">33° 52′ 7.413″ S | 152° 32′ 31.513″ E</div></div>
  <div class="reminder" style="top:358px"><div class="when">Wed, Apr 2nd at 2:00 p.m.</div><div class="gps">33° 52′ 7.413″ S | 152° 32′ 31.513″ E</div></div>
  <div class="pill" style="left:127px;top:485px;width:105px;height:37px;font-size:12px">Check-ins<svg width="11" height="9" viewBox="0 0 11 9" fill="none" stroke="#fff" stroke-width="1.2"><path d="M0 4.5h10M6 .5l4 4-4 4"/></svg></div>
</section>

</body>
</html>
```